Realtor Second mailing to my Farm Area

Doing a second mailing to my farm area. Will be sending out a postcard or some mailing every month or every other month. Going to have my companys LOGO cover a big portion of the postcard. Then my picture. Then a picture of a sold listing or area of the downtown. Also something like "My 20 Years Real Estate Experience available to you should you be thinking of Buying or Selling a home"

It Company

```html
<!DOCTYPE html>
<html lang="en">
<head>
<meta charset="utf-8">
<title>Buying or Selling a Home – Realtor Postcard</title>
<link href="https://fonts.googleapis.com/css2?family=Tinos:wght@700&family=PT+Sans+Narrow:wght@400;700&display=swap" rel="stylesheet">
<style>
  :root {
    --page-bg: #efe9e1;
    --card-white: #ffffff;
    --panel-mint: #dcebc6;
    --panel-black: #050505;
    --brand-green: #3cb44a;
    --deep-green: #1f6b2e;
    --ink: #111111;
    --stamp-grey: #d0d0d0;
    --rule-grey: #b9b9b9;
  }
  * { margin: 0; padding: 0; box-sizing: border-box; }
  html, body {
    width: 1156px;
    height: 1200px;
    overflow: hidden;
    background: var(--page-bg);
  }
  .postcard {
    position: absolute;
    left: 102px;
    width: 952px;
    border-radius: 16px;
    overflow: hidden;
    box-shadow: 0 4px 10px rgba(0,0,0,0.28);
    background: var(--card-white);
  }
  .postcard--front { top: 102px; height: 452px; }
  .postcard--back  { top: 610px; height: 453px; }

  .shape-layer { position: absolute; inset: 0; }

  /* Front */
  .front__accent { position: absolute; left: 0; top: 0; width: 22px; height: 100%; background: var(--brand-green); }
  .front__intro {
    position: absolute; left: 22px; top: 0; width: 364px; height: 100%;
    background: var(--panel-mint);
  }
  .front__headline {
    position: absolute; left: 0; right: 0; top: 22px;
    font-family: "Tinos", "Times New Roman", serif;
    font-weight: 700; font-size: 38px; line-height: 54px;
    color: var(--deep-green); text-align: center;
  }
  .front__logo {
    position: absolute; left: 0; right: 0; top: 203px;
    font-family: "Tinos", "Times New Roman", serif;
    font-weight: 700; font-size: 29px;
    color: var(--deep-green); text-align: center;
  }
  .contact {
    position: absolute;
    font-family: "PT Sans Narrow", "Arial Narrow", sans-serif;
    white-space: nowrap;
  }
  .contact__label { font-size: 23px; font-weight: 400; }
  .contact__number { font-size: 33px; font-weight: 700; }
  .front__contact { left: 30px; top: 380px; color: var(--deep-green); }

  .front__house-photo {
    position: absolute; left: 520px; top: 0; width: 432px; height: 100%;
    background: linear-gradient(180deg, #7f9a68 0%, #4f6a3c 14%, #8a4634 28%, #7a3a2a 58%, #8a5a3c 72%, #5e9a3a 82%, #7cb84c 100%);
  }
  .front__quote {
    position: absolute; left: 386px; top: 28px; width: 220px;
    font-family: "Tinos", "Times New Roman", serif;
    font-weight: 700; font-size: 29px; line-height: 43.3px;
    color: var(--brand-green); text-align: center;
    white-space: nowrap;
  }

  /* Back */
  .back__hands-photo {
    position: absolute; left: 0; top: 0; width: 282px; height: 234px;
    background: radial-gradient(ellipse at 45% 40%, #c8583a 0%, #d98a6a 35%, #f1d2c2 65%, #ffffff 100%);
  }
  .back__family-photo {
    position: absolute; left: 318px; top: 0; width: 264px; height: 436px;
    background: radial-gradient(ellipse at 55% 50%, #6b8fb5 0%, #a9bfd4 40%, #e9dccd 70%, #ffffff 100%);
  }
  .back__contact { left: 36px; top: 378px; color: var(--ink); }
  .back__stamp {
    position: absolute; left: 806px; top: 26px; width: 114px; height: 102px;
    background: var(--stamp-grey); border-radius: 8px;
  }
  .back__address-line {
    position: absolute; left: 672px; width: 248px; height: 1px;
    background: var(--rule-grey);
  }
</style>
</head>
<body>

  <section class="postcard postcard--front" aria-label="Postcard front">
    <div class="front__house-photo" role="img" aria-label="Photo of a red brick two-storey house with white trim and a green lawn"></div>
    <svg class="shape-layer" width="952" height="452" viewBox="0 0 952 452" aria-hidden="true">
      <path d="M386 0 H606 V372 Q606 446 528 452 H386 Z" fill="var(--panel-black)"/>
      <path d="M606 0 H624 V372 Q624 452 540 452 H510 Q606 446 606 372 Z" fill="var(--brand-green)"/>
    </svg>
    <div class="front__accent"></div>
    <div class="front__intro">
      <h1 class="front__headline">Buying or Selling<br>a home</h1>
      <p class="front__logo">LOGO here</p>
      <p class="contact front__contact"><span class="contact__label">Contact us - </span><span class="contact__number">(0555 318 260)</span></p>
    </div>
    <p class="front__quote">My 20 Years<br>Real Estate<br>Experience<br>available to<br>you should<br>you be think-<br>ing of Buying<br>or Selling a<br>home"</p>
  </section>

  <section class="postcard postcard--back" aria-label="Postcard back">
    <div class="back__hands-photo" role="img" aria-label="Photo of cupped hands holding a small model house with a red roof"></div>
    <div class="back__family-photo" role="img" aria-label="Photo of a smiling family of four standing together"></div>
    <svg class="shape-layer" width="952" height="453" viewBox="0 0 952 453" aria-hidden="true">
      <path d="M588 0 H606 V372 Q606 453 520 453 H494 Q588 446 588 372 Z" fill="var(--brand-green)"/>
    </svg>
    <p class="contact back__contact"><span class="contact__label">Contact us - </span><span class="contact__number">(0555 318 260)</span></p>
    <div class="back__stamp"></div>
    <div class="back__address-line" style="top:284px"></div>
    <div class="back__address-line" style="top:310px"></div>
    <div class="back__address-line" style="top:338px"></div>
    <div class="back__address-line" style="top:364px"></div>
  </section>

</body>
</html>
```